Lumora Flow Collective Business Cards

I need business cards for staff in a new startup. Our company name is MorvaLeap - we train Tai Chi teachers. But our biggest project is called Lumora Flow Collective - a federal project to put together free Tai Chi classes for Vets all across America. It's a young company, with a spirit of excitement, passion, a desire to do good for others (our Vets) and a modern style and sensibility. In other words, not old-fashioned Asian martial arts theme, but something new.

Industry/Entity Type

Health And Wellness

Contact Information for Business Card

The topic is ancient healing, but the company is the Quibbletons - so I'd like a card design that captures that.

Font styles to use
Sans Serif

Colors

Designer to choose colors to be used in the design.

Requirements
Nice to have
• I've got two logos - one for the company and one for the project. I want to see if we can incorporate them both without it becoming too busy.
Should not have
• Overly old-fashioned yin-yang themes.

```html
<!DOCTYPE html>
<html lang="en">
<head>
<meta charset="utf-8">
<title>Lumora Flow Collective Business Cards</title>
<link href="https://fonts.googleapis.com/css2?family=Montserrat:wght@400;500;700&display=swap" rel="stylesheet">
<style>
  :root {
    --stage: #e4e5e7;
    --card-dark: #1c1c1c;
    --card-light: #ffffff;
    --navy: #232a6e;
    --red: #d8202a;
    --cream: #f3ea9c;
    --ink: #3a3a3a;
    --rule: #8a8a8a;
  }
  * { box-sizing: border-box; margin: 0; padding: 0; }
  html, body {
    width: 1200px; height: 874px; overflow: hidden;
    background: var(--stage);
    font-family: "Montserrat", sans-serif;
  }
  .stage {
    width: 1200px; height: 874px;
    display: flex; align-items: center; justify-content: center; gap: 40px;
  }
  .card {
    width: 540px; height: 309px;
    border-radius: 18px;
    position: relative;
    box-shadow: 0 10px 28px rgba(0,0,0,.18);
    overflow: hidden;
  }
  /* Back side */
  .card--back {
    background: var(--card-dark);
    display: flex; flex-direction: column; align-items: center; justify-content: center;
  }
  .brand {
    display: flex; align-items: center; gap: 14px;
    margin-top: -20px;
  }
  .brand__dot {
    width: 46px; height: 46px; border-radius: 50%;
    background: var(--red);
  }
  .brand__name {
    font-weight: 700; font-size: 34px; color: var(--cream);
    letter-spacing: .5px;
  }
  .card--back .url {
    position: absolute; bottom: 42px; left: 0; right: 0;
    text-align: center; color: #f2f2f2; font-size: 13px; letter-spacing: .3px;
  }
  /* Front side */
  .card--front {
    background: var(--card-light);
    display: flex; align-items: center;
  }
  .project {
    width: 268px; display: flex; align-items: center; justify-content: center; gap: 10px;
    padding-left: 12px;
  }
  .project__dot {
    width: 26px; height: 26px; border-radius: 50%;
    border: 3px solid var(--navy); flex: none;
  }
  .project__name {
    font-weight: 700; font-size: 17px; line-height: 1.2; color: var(--navy);
    text-transform: uppercase;
  }
  .divider {
    width: 1px; height: 200px; background: var(--rule); flex: none;
  }
  .contact { padding-left: 26px; color: var(--ink); }
  .contact__name {
    font-weight: 700; font-size: 20px; color: var(--navy);
    text-transform: uppercase; letter-spacing: .3px;
  }
  .contact__role { font-size: 12.5px; margin-top: 2px; }
  .contact__address { font-size: 12.5px; line-height: 1.35; margin-top: 18px; }
  .contact__list { list-style: none; margin-top: 16px; font-size: 12.5px; }
  .contact__list li { display: flex; align-items: center; gap: 10px; line-height: 1.6; }
  .contact__list svg { width: 13px; height: 13px; flex: none; }
</style>
</head>
<body>
<main class="stage">
  <section class="card card--back">
    <div class="brand">
      <span class="brand__dot"></span>
      <span class="brand__name">MorvaLeap</span>
    </div>
    <p class="url">https://www.morvaleap.net/vets</p>
  </section>

  <section class="card card--front">
    <div class="project">
      <span class="project__dot"></span>
      <span class="project__name">Lumora Flow<br>Collective</span>
    </div>
    <span class="divider"></span>
    <div class="contact">
      <h1 class="contact__name">Darren Holloway</h1>
      <p class="contact__role">Managing Partner</p>
      <p class="contact__address">2718 Fenwick Ave. Ste. 204<br>Harbor Vale<br>CA 90412</p>
      <ul class="contact__list">
        <li>
          <svg viewBox="0 0 24 24" aria-hidden="true"><path fill="#d8202a" d="M6.6 10.8a15.1 15.1 0 0 0 6.6 6.6l2.2-2.2a1 1 0 0 1 1-.25 11.4 11.4 0 0 0 3.6.57 1 1 0 0 1 1 1V20a1 1 0 0 1-1 1A17 17 0 0 1 3 4a1 1 0 0 1 1-1h3.5a1 1 0 0 1 1 1c0 1.25.2 2.45.57 3.6a1 1 0 0 1-.25 1z"/></svg>
          555-204-7781
        </li>
        <li>
          <svg viewBox="0 0 24 24" aria-hidden="true"><rect x="2.5" y="5" width="19" height="14" rx="1" fill="none" stroke="#d8202a" stroke-width="2.2"/><path d="M3 6l9 7 9-7" fill="none" stroke="#d8202a" stroke-width="2.2"/></svg>
          info@morvaleap.net
        </li>
        <li>
          <svg viewBox="0 0 24 24" aria-hidden="true"><g fill="none" stroke="#d8202a" stroke-width="2"><circle cx="12" cy="12" r="9.5"/><ellipse cx="12" cy="12" rx="4" ry="9.5"/><path d="M2.5 12h19M4 7h16M4 17h16"/></g></svg>
          www.morvaleap.net
        </li>
      </ul>
    </div>
  </section>
</main>
</body>
</html>
```